Flyer für Onlineshop
Zielgruppe
Wir vertreiben 2 Komponentenlacke, wasserbasiert, auf Polyurethanharz Basis zur Sanierung von Fliesen vieles und mehr.
Aufgabenstellung
Wir möchten eine Fleyer speziell für die Fliesenfarben.
Das Design soll frisch, modern und ansprechend gestaltet sein. Wir möchten den Fleyer öffentlich auslegen aber auch an z.B Jugendherbergen, Kurhäuser ect. und privat Personen verteilen um darauf aufmerksam zu machen das es eine güstige alternative zum Neukauf gibt.
Auf dem Flyer soll in der Fliesenlack im Vordergrund stehen es darf aber kurz auf weitere Produkte aufmerksam gemacht werden.
für die Größe des Flyers habe ich keine genauen Vorstellungen lasse mich überraschen.
Sie finden die Informationen die Sie benötigen unter
www.ralbo-sonderlacke.com/farben-lacke/fliesenfarbe
Der Fleyer sollte die Maße DIN lang (105 x 210 mm) hoch / 4 Seiten
Aber auch andere Vorschläge sind Willkommen
Also Logo habe ich verschiedene jpg´s hochgeladen..leider ist die qualität nicht sehr gut aber vielleicht können Sie was damit anfangen.
Bei weiteren Fragen stehe ich Ihnen gerne zur Verfügung

```html
<!DOCTYPE html>
<html lang="de">
<head>
<meta charset="utf-8">
<title>Die Fliesenfarbe – Flyer</title>
<link rel="stylesheet" href="https://fonts.googleapis.com/css2?family=Oswald:wght@300;400&family=PT+Sans:wght@400;700&display=swap">
<style>
  :root {
    --paper: #ffffff;
    --panel: #d6dee4;
    --accent-blue: #2f7fd8;
    --accent-red: #c8401f;
    --ink: #1c1c1c;
    --tile-a: #b0563a;
    --tile-b: #d9c6a8;
    --paint-a: #3f8f86;
    --paint-b: #e8ece9;
    --bath-a: #c9b37a;
    --bath-b: #d24a3a;
  }
  * { margin: 0; padding: 0; box-sizing: border-box; }
  html, body { width: 1137px; height: 1200px; overflow: hidden; background: var(--paper); }
  .flyer { position: relative; width: 1137px; height: 1200px; color: var(--ink);
    font-family: "PT Sans", Arial, sans-serif; font-size: 17.5px; line-height: 30px; }
  .tab { position: absolute; background: var(--accent-blue); }
  .title { position: absolute; left: 79px; top: 70px; font-family: "Oswald", sans-serif; font-weight: 300;
    font-size: 58px; line-height: 64px; letter-spacing: 2px; }
  .title .initial { color: var(--accent-red); font-weight: 400; }
  .lead { position: absolute; left: 79px; top: 136px; font-weight: 700; font-size: 18px; }
  .copy { position: absolute; text-align: justify; }
  .copy b { font-weight: 700; }
  .intro { left: 79px; top: 190px; width: 468px; }
  .benefits { left: 79px; top: 718px; width: 468px; }
  .photo { position: absolute; }
  .tiles { left: 39px; top: 432px; width: 501px; height: 272px;
    background: linear-gradient(135deg, var(--tile-b) 0%, var(--tile-a) 35%, #c98a5c 55%, var(--tile-b) 75%, #8a3b28 100%); }
  .panel { position: absolute; left: 585px; top: 55px; width: 552px; height: 1145px; background: var(--panel); }
  .painting { left: 619px; top: 88px; width: 442px; height: 236px;
    background: linear-gradient(90deg, var(--paint-a) 0%, #6fb0a6 45%, var(--paint-b) 55%, #ffffff 100%); }
  .panel-heading { position: absolute; left: 619px; top: 356px; font-family: "Oswald", sans-serif; font-weight: 300;
    font-size: 35px; line-height: 48px; color: var(--accent-blue); letter-spacing: 1.5px; }
  .panel-sub { position: absolute; left: 619px; top: 408px; font-weight: 700; font-size: 17.5px; }
  .finish-list { position: absolute; left: 668px; top: 457px; list-style: none; line-height: 28px; }
  .panel-copy { left: 619px; top: 572px; width: 482px; }
  .panel-copy .web { font-weight: 700; }
  .bathroom { left: 619px; top: 874px; width: 442px; height: 296px;
    background: linear-gradient(160deg, var(--bath-a) 0%, #e7d9b5 40%, var(--bath-b) 70%, #f0a030 100%); }
</style>
</head>
<body>
<div class="flyer">
  <div class="tab" style="left:35px;top:0;width:34px;height:49px"></div>
  <h1 class="title"><span class="initial">D</span>IE FLIESENFARBE</h1>
  <p class="lead">Ihres Bades oder Ihrer Küche gefällt Ihnen nicht mehr?</p>
  <p class="copy intro">Das ist kein Grund zum Verzagen, denn mit dem Fliesenlack aus dem <b>Ralbo-Sonderlacke-Sortiment</b>, kann Ihr Bad und Ihre Küche schon bald <b>in Ihrer Lieblingsfarbe</b> erstrahlen. Verzichten Sie darauf, die in die Jahre gekommenen Fliesen <b>abzuschlagen</b> und anschließend <b>neue Fliesen verlegen</b> zu lassen! So eine <b>Renovierung kostet</b> nicht nur sehr viel Geld, sie verursacht auch viel <b>Staub und Lärm.</b></p>

  <div class="photo tiles" role="img" aria-label="Diagonal verlegte Fliesen in Rot-, Braun- und Beigetönen"></div>
  <div class="tab" style="left:540px;top:432px;width:20px;height:90px"></div>

  <p class="copy benefits">Ob in <b>Bad</b>, <b>Küche</b> oder <b>Lagerraum</b>, Fliesen haben ohne Zweifel einen hohen praktischen Nutzen. Direkt nach dem Kauf findet man sie meist sehr schön. <b>Mit der Zeit jedoch verblasst oft ihr Glanz oder ihr Design kommt aus der Mode.</b> Es ist nicht unüblich, dass sich der persönliche Geschmack mit den Jahren wandelt. Wer Ralbo Fliesenfarbe verwendet, begegnet diesem Umstand, <b>ohne eine aufwändige Sanierung</b> mit teuren neuen Fliesen vornehmen zu müssen. <b>Lärm, Staub und Schmutz</b> durch einen Fliesenwechsel <b>müssen nicht sein,</b> denn unsere Fliesenlacke <b>haften und decken sehr gut, wobei sie wasserverdünnbar auf der Basis einer Kunststoffdispersion</b> sind. Gegen <b>Licht, Wetter und Chemikalien bestehen die Spezialfarben ebenfalls.</b> Je nach Variante bleibt der Farbton dabei <b>matt</b> oder <b>glänzt</b> ansprechend.</p>

  <div class="panel"></div>
  <div class="photo painting" role="img" aria-label="Hände streichen Wandfliesen mit Farbrolle in Türkis und Weiß"></div>
  <div class="tab" style="left:1061px;top:88px;width:35px;height:128px"></div>
  <h2 class="panel-heading">GEBRAUCHSFERTIGE FLIESENFARBEN</h2>
  <p class="panel-sub">in vielen schönen Farbvariationen</p>
  <div class="tab" style="left:619px;top:458px;width:19px;height:72px"></div>
  <ul class="finish-list">
    <li>seidenglänzend für ein apartes Badezimmer</li>
    <li>matt für Keller oder Garage</li>
    <li>hochglänzend für Bad oder Küche</li>
  </ul>
  <p class="copy panel-copy">Dabei stehen <b>zahlreiche Farbtöne</b> zur Auswahl, damit für jeden Möbelstil und jeden Geschmack das Passende gefunden werden kann. Neben <b>helleren und dunkleren</b> Varianten sind <b>kalte und warme Töne</b> verfügbar. Bevor der Decklack aufgetragen werden kann, sind eine reinigende Vorbehandlung, das Trocknen und der Auftrag der Grundierung nötig. Die dafür nötigen Produkte lassen sich separat <b>in unserem Onlineshop</b> erwerben.<br>Wir beraten Sie gerne! Besuchen Sie uns einfach auf<br><span class="web">www.ralbo-sonderlacke.com</span></p>
  <div class="photo bathroom" role="img" aria-label="Badezimmer mit Badewanne und bunt gestrichenen Wandfliesen"></div>
  <div class="tab" style="left:1061px;top:874px;width:29px;height:147px"></div>
</div>
</body>
</html>
```